Modern HomePage Design for Church

We are looking for a modern homepage design using the sections we put together in the template. The colors we want are blue, black, grey, and white. We do not want use the colors in the logo. Please modify the logo color to match the website color scheme.

Target Market(s)

Church

Industry/Entity Type

Church

Number of Pages Required

1 page

Colors
0293ce
ffffff
474747
9d9d9d

```html
<!DOCTYPE html>
<html lang="en">
<head>
<meta charset="utf-8">
<title>Riverstone Church — Home</title>
<link href="https://fonts.googleapis.com/css2?family=Montserrat:wght@400;600;700;800&family=Open+Sans:wght@400;600;700&family=Roboto+Slab:wght@400;700&family=Playfair+Display:ital,wght@1,700&display=swap" rel="stylesheet">
<style>
:root{
  --blue:#0293ce;
  --blue-dark:#0a5f86;
  --ink:#1b1b1b;
  --charcoal:#474747;
  --grey:#9d9d9d;
  --light:#f1f1f1;
  --white:#ffffff;
  --night:#141414;
}
*{margin:0;padding:0;box-sizing:border-box}
html,body{width:1200px;height:3316px;overflow:hidden;background:var(--white)}
body{font-family:"Open Sans",Arial,sans-serif;color:var(--charcoal);position:relative}
.section{position:absolute;left:0;width:1200px;overflow:hidden}
.abs{position:absolute}
.btn{display:inline-block;font-family:"Montserrat",sans-serif;font-weight:700;font-size:10px;letter-spacing:1px;text-transform:uppercase;padding:9px 20px;color:var(--white);background:var(--blue)}
.btn-dark{background:var(--ink)}
.btn-ghost{background:transparent;border:1px solid var(--white)}
.slab{font-family:"Roboto Slab",Georgia,serif}
.mont{font-family:"Montserrat",sans-serif}

/* header + hero */
.hero{top:0;height:480px}
.hero-photo{position:absolute;inset:0;background:linear-gradient(100deg,#4a1208 0%,#9c3a16 30%,#c7652a 55%,#7a2a12 80%,#2d0d07 100%)}
.hero-shade{position:absolute;inset:0;background:linear-gradient(180deg,rgba(0,0,0,.35),rgba(0,0,0,.1) 40%,rgba(0,0,0,.35))}
.topbar{position:absolute;top:0;left:0;width:1200px;height:46px;background:rgba(10,10,10,.92)}
.nav{position:absolute;left:120px;top:0;display:flex;height:46px;align-items:center;gap:32px}
.nav a{font-family:"Montserrat",sans-serif;font-size:10px;font-weight:600;color:var(--white);text-decoration:none;letter-spacing:.8px}
.nav a.active{color:var(--blue)}
.topbar .btn{position:absolute;right:170px;top:9px;padding:8px 18px}
.sub-links{position:absolute;right:120px;top:56px;display:flex;gap:6px}
.sub-links span{font-family:"Montserrat",sans-serif;font-size:8px;font-weight:600;color:var(--white);background:rgba(0,0,0,.55);padding:5px 9px;letter-spacing:.5px}
.brand{position:absolute;left:40px;top:72px;display:flex;align-items:center;gap:10px}
.brand i{width:14px;height:14px;border-radius:50%;background:var(--blue);display:block}
.brand b{font-family:"Roboto Slab",serif;font-weight:700;font-size:30px;color:var(--white);letter-spacing:2px}
.hero-text{position:absolute;left:500px;top:292px;width:360px;text-align:center;color:var(--white)}
.hero-text h1{font-family:"Montserrat",sans-serif;font-weight:800;font-size:44px;letter-spacing:1px;line-height:1}
.hero-text h2{font-family:"Montserrat",sans-serif;font-weight:700;font-size:18px;margin-top:8px;letter-spacing:1px}
.hero-text p{font-family:"Montserrat",sans-serif;font-size:12px;font-weight:600;letter-spacing:2px;margin-top:6px}
.hero-text .btn{margin-top:24px;background:rgba(0,0,0,.55);border:1px solid var(--white)}

/* welcome */
.welcome{top:480px;height:340px;background:var(--white)}
.welcome h2{position:absolute;left:200px;top:40px;font-family:"Roboto Slab",serif;font-size:27px;color:var(--ink);font-weight:700}
.welcome .lead{position:absolute;left:200px;top:84px;width:580px;font-family:"Montserrat",sans-serif;font-weight:700;font-size:10px;color:var(--blue);letter-spacing:.4px}
.welcome .copy{position:absolute;left:200px;top:110px;width:580px;font-size:11px;line-height:1.6;color:var(--charcoal)}
.welcome .copy p+p{margin-top:14px}
.pastor-photo{position:absolute;left:820px;top:30px;width:200px;height:270px;background:linear-gradient(160deg,#e9eef2,#b9c2cc 60%,#5a4a40)}
.signature{position:absolute;left:200px;top:268px;width:580px;text-align:center;font-family:"Playfair Display",serif;font-style:italic;font-weight:700;font-size:32px;color:var(--ink)}
.signature::before,.signature::after{content:"";display:inline-block;width:70px;height:1px;background:var(--ink);vertical-align:middle;margin:0 14px}

/* meeting */
.meeting{top:820px;height:160px;background:linear-gradient(90deg,#0b0b0b,#222 50%,#0d0d0d)}
.meeting-head{position:absolute;left:200px;top:40px;width:380px;text-align:center;color:var(--white)}
.meeting-head h3{font-family:"Roboto Slab",serif;font-size:22px;font-weight:700}
.meeting-head .date{font-family:"Montserrat",sans-serif;font-size:10px;color:var(--blue);font-weight:700;margin-top:6px}
.meeting-head p{font-size:10px;color:#cfcfcf;margin-top:10px;line-height:1.5}
.countdown{position:absolute;left:700px;top:36px;display:flex;gap:12px}
.countdown div{width:50px;text-align:center;color:var(--white)}
.countdown small{display:block;font-size:8px;color:var(--grey);font-weight:700;letter-spacing:.5px}
.countdown b{display:block;font-family:"Montserrat",sans-serif;font-size:26px;font-weight:800;margin-top:2px}
.meeting .btn{position:absolute;left:826px;top:108px}

/* features */
.features{top:980px;height:480px;background:linear-gradient(160deg,#0e4766,#0a3149 55%,#0c3c58)}
.features-shade{position:absolute;inset:0;background:radial-gradient(circle at 70% 30%,rgba(2,147,206,.25),transparent 60%)}
.feature{position:absolute;top:100px;width:260px;text-align:center;color:var(--white)}
.feature svg{display:block;margin:0 auto}
.feature h4{font-family:"Roboto Slab",serif;font-size:17px;font-weight:700;margin-top:30px;letter-spacing:.5px}
.feature p{font-size:10px;line-height:1.6;color:#d3e3ec;margin-top:14px;height:60px}
.feature .btn{margin-top:38px}

/* involve */
.involve{top:1460px;height:372px;background:var(--white)}
.photo-grid{position:absolute;left:200px;top:12px;width:480px;height:340px;display:grid;grid-template-columns:1fr 1fr;grid-template-rows:1fr 1fr;gap:4px}
.tile{position:relative}
.tile .btn{position:absolute;left:78px;top:22px;font-size:8px;padding:6px 12px}
.t1{background:linear-gradient(135deg,#c9d8e6,#5b7fa3)}
.t2{background:linear-gradient(135deg,#e3c9a3,#8a5a32)}
.t3{background:linear-gradient(135deg,#d89a6a,#6b3a1f)}
.t4{background:linear-gradient(135deg,#4f6f96,#c8d7ec)}
.involve-panel{position:absolute;left:688px;top:12px;width:312px;height:340px;background:var(--blue);color:var(--white);padding:64px 40px}
.involve-panel h3{font-family:"Montserrat",sans-serif;font-size:22px;font-weight:700}
.involve-panel p{font-size:11px;line-height:1.6;margin-top:16px}
.involve-panel .btn{margin-top:40px;background:var(--ink)}

/* blog / pray */
.blogrow{top:1832px;height:300px;background:var(--white)}
.blog-head{position:absolute;left:200px;top:6px;width:310px;height:74px;background:var(--ink);color:var(--white);padding:22px 30px;font-family:"Roboto Slab",serif;font-weight:700;font-size:26px}
.blog-card{position:absolute;left:200px;top:80px;width:310px;height:200px;background:var(--blue);color:var(--white);padding:28px 30px}
.blog-card h4{font-family:"Montserrat",sans-serif;font-weight:700;font-size:18px}
.blog-card p{font-size:10px;line-height:1.6;margin-top:10px}
.pray{position:absolute;left:530px;top:6px;width:470px}
.pray h3{font-family:"Roboto Slab",serif;font-weight:700;font-size:27px;color:var(--ink)}
.pray .rule{width:470px;height:3px;background:var(--blue);margin-top:6px}
.pray p{font-size:10px;line-height:1.6;margin-top:16px;color:var(--charcoal)}
.pray .btn{margin-top:24px;background:var(--ink)}

/* pastor + sermons */
.word{top:2132px;height:348px;background:linear-gradient(120deg,#3a3a3a,#6b6b6b 45%,#3c3c3c)}
.word-shade{position:absolute;inset:0;background:rgba(0,0,0,.35)}
.label{position:absolute;font-family:"Montserrat",sans-serif;font-weight:700;font-size:10px;color:var(--blue);letter-spacing:1px}
.label::after{content:"";display:block;width:300px;height:1px;background:rgba(255,255,255,.35);margin-top:6px}
.word .face-box{position:absolute;left:200px;top:70px;width:190px;height:230px;background:linear-gradient(160deg,#d9d2c9,#8a7c70 60%,#3f3a36)}
.quote{position:absolute;left:410px;top:78px;width:200px;color:var(--white)}
.quote h4{font-family:"Roboto Slab",serif;font-weight:700;font-size:22px;line-height:1.25}
.quote p{font-size:9.5px;line-height:1.6;margin-top:14px;color:#e2e2e2}
.sermons{position:absolute;left:700px;top:64px;width:300px}
.sermon{display:flex;align-items:center;gap:14px;height:44px;margin-bottom:14px;border-bottom:1px solid rgba(255,255,255,.2)}
.sermon i{width:26px;height:26px;background:rgba(0,0,0,.6);display:flex;align-items:center;justify-content:center}
.sermon span{font-family:"Montserrat",sans-serif;font-weight:700;font-size:10px;color:var(--white);letter-spacing:.4px}

/* events */
.events{top:2480px;height:500px;background:var(--white)}
.event{position:absolute;width:380px;height:200px;display:flex}
.event-img{width:180px;height:200px;position:relative}
.e1{background:linear-gradient(135deg,#b33a24,#5c1d12)}
.e2{background:linear-gradient(135deg,#a33b28,#4a1a10)}
.event-img .day{position:absolute;left:0;bottom:0;width:180px;height:44px;background:var(--white);display:flex;align-items:center;justify-content:space-between;padding:0 0 0 0}
.day b{font-family:"Montserrat",sans-serif;font-weight:800;font-size:20px;color:var(--blue);padding-left:12px}
.day .btn{font-size:8px;padding:8px 12px;background:var(--ink);margin-right:6px}
.event-body{padding:4px 0 0 18px;width:200px}
.event-body h5{font-family:"Montserrat",sans-serif;font-weight:700;font-size:12px;color:var(--ink);line-height:1.35}
.event-body ul{list-style:none;margin-top:12px}
.event-body li{font-size:9.5px;color:var(--charcoal);display:flex;align-items:center;gap:8px;margin-bottom:7px}
.event-body li i{width:8px;height:8px;border-radius:50%;background:var(--blue);display:block;flex:none}

/* footer */
.footer{top:2980px;height:336px;background:linear-gradient(180deg,#242424,#111)}
.fcol{position:absolute;top:36px;width:260px}
.fcol h6{font-family:"Montserrat",sans-serif;font-weight:700;font-size:9px;color:var(--white);letter-spacing:1px;padding-bottom:8px;border-bottom:1px solid rgba(255,255,255,.15)}
.fpost{display:flex;gap:12px;margin-top:16px}
.fpost .thumb{width:44px;height:44px;flex:none;background:linear-gradient(135deg,#8a5a3a,#3b2519)}
.fpost b{display:block;font-family:"Montserrat",sans-serif;font-size:9px;color:var(--blue);font-weight:700}
.fpost span{font-size:9px;color:var(--grey);line-height:1.5}
.tags{display:flex;flex-wrap:wrap;gap:6px;margin-top:16px}
.tags span{font-family:"Montserrat",sans-serif;font-size:8px;font-weight:600;color:var(--white);background:var(--blue);padding:5px 9px}
.copyright{position:absolute;left:0;width:1200px;top:290px;text-align:center;font-size:9px;color:var(--grey);border-top:1px solid rgba(255,255,255,.1);padding-top:14px}
</style>
</head>
<body>

<header class="section hero">
  <div class="hero-photo" role="img" aria-label="Photo of a smiling couple embracing outdoors in warm light"></div>
  <div class="hero-shade"></div>
  <div class="topbar">
    <nav class="nav">
      <a class="active">HOME</a><a>ABOUT</a><a>MINISTRIES</a><a>EVENTS</a><a>SERMONS</a><a>CONTACTS</a><a>BLOG</a>
    </nav>
    <span class="btn">Donate Now</span>
  </div>
  <div class="sub-links"><span>PLAN YOUR VISIT</span><span>LIVE STREAM</span></div>
  <div class="brand"><i></i><b>WELLSPRING</b></div>
  <div class="hero-text">
    <h1>COUPLES CAMP</h1>
    <h2>CONNECT &amp; GROW TOGETHER</h2>
    <p>REGISTRATION NOW OPEN</p>
    <span class="btn">Learn More</span>
  </div>
</header>

<section class="section welcome">
  <h2>WELCOME TO RIVERSTONE CHURCH</h2>
  <div class="lead">WE ARE A COMMUNITY THAT GATHERS TO WORSHIP, GROW AND SERVE TOGETHER IN FAITH</div>
  <div class="copy">
    <p>Every week we open our doors to families, friends and neighbours who are seeking hope, rest and a place to belong. Our worship is simple, joyful and rooted in scripture, and our small groups meet across the city to pray, study and share life with one another.</p>
    <p>Whether you are new to faith or have walked with God for years, there is room for you here. Come as you are, bring your questions, and discover a church family that will walk with you every step of the way.</p>
  </div>
  <div class="pastor-photo" role="img" aria-label="Portrait of the senior pastor and his wife"></div>
  <div class="signature">Pastor Reed</div>
</section>

<section class="section meeting">
  <div class="meeting-head">
    <h3>CHURCH LEADERS MEETING</h3>
    <div class="date">March 21, 2018 7:00 pm</div>
    <p>Meeting for the church leaders. This time we plan the strategy for the church and give feedback on projects.</p>
  </div>
  <div class="countdown">
    <div><small>DAYS</small><b>06</b></div>
    <div><small>HOURS</small><b>06</b></div>
    <div><small>MINS</small><b>06</b></div>
    <div><small>SECS</small><b>06</b></div>
  </div>
  <span class="btn">Read More</span>
</section>

<section class="section features">
  <div class="features-shade"></div>
  <div class="feature" style="left:122px">
    <svg width="56" height="56" viewBox="0 0 56 56" fill="none" stroke="#fff" stroke-width="2.4" stroke-linejoin="round"><path d="M28 48 9 29a11 11 0 0 1 19-13 11 11 0 0 1 19 13Z"/><path d="M10 28h10l4-7 5 13 4-6h13"/></svg>
    <h4>WHAT WE BELIEVE</h4>
    <p>We believe in one God who made all things and who loves the world. Read our full statement of faith and the story of our church.</p>
    <span class="btn">Read More</span>
  </div>
  <div class="feature" style="left:470px">
    <svg width="56" height="56" viewBox="0 0 56 56" fill="none" stroke="#fff" stroke-width="2.4" stroke-linecap="round"><circle cx="28" cy="28" r="22"/><path d="M28 14v14l10 6"/></svg>
    <h4>SERVICES &amp; LOCATION</h4>
    <p>Sunday Worship 9:00 AM &amp; 11:00 AM<br>Wednesday Prayer 7:00 PM<br>240 Maple Hollow Road, Brookfield</p>
    <span class="btn">Read More</span>
  </div>
  <div class="feature" style="left:800px">
    <svg width="56" height="56" viewBox="0 0 56 56" fill="none" stroke="#fff" stroke-width="2.4" stroke-linejoin="round" stroke-linecap="round"><path d="M28 26 20 18a5 5 0 0 1 8-6 5 5 0 0 1 8 6Z"/><path d="M6 36h10l8 4h10a3 3 0 0 1 0 6H24M34 44l12-6a3 3 0 0 1 4 4L34 50H16l-10-4"/></svg>
    <h4>WATCH LIVE</h4>
    <p>Join our services from anywhere. Stream every Sunday service and catch up on past messages whenever you like.</p>
    <span class="btn">Watch Live</span>
  </div>
</section>

<section class="section involve">
  <div class="photo-grid">
    <div class="tile t1" role="img" aria-label="Photo of a child smiling outdoors"><span class="btn">Kids</span></div>
    <div class="tile t2" role="img" aria-label="Photo of a family walking together"><span class="btn">Families</span></div>
    <div class="tile t3" role="img" aria-label="Photo of young people worshipping"><span class="btn">Youth</span></div>
    <div class="tile t4" role="img" aria-label="Photo of a couple by the water"><span class="btn">Adults</span></div>
  </div>
  <div class="involve-panel">
    <h3>GET INVOLVED</h3>
    <p>"The success of our church depends on participation from people like you. Get involved in our ministries — it will change your life."</p>
    <span class="btn">Read More</span>
  </div>
</section>

<section class="section blogrow">
  <div class="blog-head">BLOG</div>
  <div class="blog-card">
    <h4>GET INVOLVED</h4>
    <p>The success of our church depends on participation from people like you. Get involved in our ministries — it will change your life.</p>
  </div>
  <div class="pray">
    <h3>PRAY WITHOURT CEASING</h3>
    <div class="rule"></div>
    <p>Prayer is the heartbeat of a living church. When we pray together we are reminded that we are not alone, that God hears us, and that every burden can be carried to Him. Our prayer teams meet each week and welcome anyone who wishes to join them in quiet worship and intercession.</p>
    <p>Send us your requests through the prayer wall or speak to one of our ministers after the service. Every request is held in confidence and lifted up in love by our caring team.</p>
    <span class="btn">Read More</span>
  </div>
</section>

<section class="section word">
  <div class="word-shade"></div>
  <div class="label" style="left:200px;top:30px">PASTOR</div>
  <div class="label" style="left:700px;top:30px">SERMONS</div>
  <div class="face-box" role="img" aria-label="Portrait of the pastor"></div>
  <div class="quote">
    <h4>"One thing I ask of the Lord"</h4>
    <p>One thing I ask of the Lord, this only do I seek: that I may dwell in the house of the Lord all the days of my life, to gaze on His beauty and to seek Him in His temple. A short word from our pastor to begin the week.</p>
  </div>
  <div class="sermons">
    <div class="sermon"><i><svg width="10" height="10" viewBox="0 0 10 10"><path d="M2 1l7 4-7 4z" fill="#fff"/></svg></i><span>HOLY SPIRIT STRATEGIC THINKING</span></div>
    <div class="sermon"><i><svg width="10" height="10" viewBox="0 0 10 10"><path d="M2 1l7 4-7 4z" fill="#fff"/></svg></i><span>HOLY SPIRIT STRATEGIC THINKING</span></div>
    <div class="sermon"><i><svg width="10" height="10" viewBox="0 0 10 10"><path d="M2 1l7 4-7 4z" fill="#fff"/></svg></i><span>HOLY SPIRIT STRATEGIC THINKING</span></div>
  </div>
</section>

<section class="section events">
  <article class="event" style="left:200px;top:20px">
    <div class="event-img e1" role="img" aria-label="Photo of a Bible held in hands"><div class="day"><b>22ND</b><span class="btn">Read More</span></div></div>
    <div class="event-body"><h5>SHARING OUR FAITH &amp; LOVE TO CHILDREN</h5><ul><li><i></i>Thursday 09:00 AM</li><li><i></i>Kings Road Church</li><li><i></i>240 Maple Hollow Rd</li></ul></div>
  </article>
  <article class="event" style="left:620px;top:20px">
    <div class="event-img e2" role="img" aria-label="Photo of a Bible held in hands"><div class="day"><b>22ND</b><span class="btn">Read More</span></div></div>
    <div class="event-body"><h5>SHARING OUR FAITH &amp; LOVE TO CHILDREN</h5><ul><li><i></i>Thursday 09:00 AM</li><li><i></i>Kings Road Church</li><li><i></i>240 Maple Hollow Rd</li></ul></div>
  </article>
  <article class="event" style="left:200px;top:250px">
    <div class="event-img e1" role="img" aria-label="Photo of a Bible held in hands"><div class="day"><b>22ND</b><span class="btn">Read More</span></div></div>
    <div class="event-body"><h5>SHARING OUR FAITH &amp; LOVE TO CHILDREN</h5><ul><li><i></i>Thursday 09:00 AM</li><li><i></i>Kings Road Church</li><li><i></i>240 Maple Hollow Rd</li></ul></div>
  </article>
  <article class="event" style="left:620px;top:250px">
    <div class="event-img e2" role="img" aria-label="Photo of a Bible held in hands"><div class="day"><b>22ND</b><span class="btn">Read More</span></div></div>
    <div class="event-body"><h5>SHARING OUR FAITH &amp; LOVE TO CHILDREN</h5><ul><li><i></i>Thursday 09:00 AM</li><li><i></i>Kings Road Church</li><li><i></i>240 Maple Hollow Rd</li></ul></div>
  </article>
</section>

<footer class="section footer">
  <div class="fcol" style="left:160px">
    <h6>LATEST SERMONS</h6>
    <div class="fpost"><div class="thumb" role="img" aria-label="Sermon thumbnail"></div><div><b>WALKING IN FAITH</b><span>A message on trust and patience in hard seasons.</span></div></div>
    <div class="fpost"><div class="thumb" role="img" aria-label="Sermon thumbnail"></div><div><b>THE GOOD SHEPHERD</b><span>Finding rest and guidance in His care.</span></div></div>
  </div>
  <div class="fcol" style="left:470px">
    <h6>BROWSE TAGS</h6>
    <div class="tags"><span>FAITH</span><span>PRAYER</span><span>WORSHIP</span><span>FAMILY</span><span>YOUTH</span><span>HOPE</span><span>GRACE</span><span>MISSIONS</span><span>EVENTS</span></div>
  </div>
  <div class="fcol" style="left:780px">
    <h6>LATEST SERMONS</h6>
    <div class="fpost"><div class="thumb" role="img" aria-label="Sermon thumbnail"></div><div><b>LOVE IN ACTION</b><span>Serving our neighbours as Christ served us.</span></div></div>
    <div class="fpost"><div class="thumb" role="img" aria-label="Sermon thumbnail"></div><div><b>A HEART OF PRAISE</b><span>Why worship shapes every part of life.</span></div></div>
  </div>
  <div class="copyright">© 2018 All Rights Reserved. Riverstone Church Community</div>
</footer>

</body>
</html>
```